7q | SOLUTIONS Biz Card Design

Seventh Quarry Solutions, LLC
7q | HOME INSPECTIONS
7q | ENVIRONMENTAL TESTING
7q | THERMOGRAPHY IMAGING
(Would like progressive design, maybe use 7q as a logo or part of logo; want to reflect healthy environments, incorporating sun, or blue skies, etc.; primary colors, one side or two is acceptable)
Updates

I'm very partial to the simple modern fonts such as Helvetica or Museo Sans 500 or the new one I've recently seen that's like Helvetica with attitude. Added Tuesday, May 5, 2015

Target Market(s)

Home owners and realtors

Industry/Entity Type

Progressive

Contact Information for Business Card

Gus Morrow, President/CEO
GusMorrow@7qSolutions.example
www.7qSolutions.example
555.014.7301
555.014.7302 fax

Font styles to use
Other font styles liked:
• Fabrica, Helvetica, Arial, Nevis, Nexa

Colors
0355a3
ec1f27
ffffff
fbed22
ffc214
9bcb3b

Requirements
Must have
• Professional yet bright colors design. Don't want to look too mom and pop.
Nice to have
• Use '7q' to create a logo.
Should not have
• Not too busy, make two-sided if there's not enough white space.

```html
<!DOCTYPE html>
<html lang="en">
<head>
<meta charset="utf-8">
<title>7q | SOLUTIONS Business Card</title>
<link rel="stylesheet" href="https://fonts.googleapis.com/css2?family=Questrial&family=Nunito+Sans:wght@700&display=swap">
<style>
  :root {
    --brand-blue: #0355a3;
    --brand-red: #ec1f27;
    --brand-white: #ffffff;
    --sun-yellow: #fbed22;
    --sun-orange: #ffc214;
    --sun-deep: #f5a21b;
    --leaf-green: #9bcb3b;
    --page: #efebe0;
    --text-font: "Questrial", "Helvetica Neue", Arial, sans-serif;
    --bold-font: "Nunito Sans", "Helvetica Neue", Arial, sans-serif;
  }
  * { box-sizing: border-box; margin: 0; padding: 0; }
  html, body { width: 1200px; height: 1000px; overflow: hidden; }
  body {
    background: var(--page);
    font-family: var(--text-font);
    position: relative;
  }
  .card {
    position: absolute;
    left: 320px;
    width: 560px;
    height: 320px;
    overflow: hidden;
    box-shadow: 0 6px 18px rgba(0,0,0,.18);
  }

  /* Front side */
  .card--front {
    top: 120px;
    background: linear-gradient(to bottom,
      #2a6fc0 0%, #8fb2de 22%, #e6eef8 42%, #ffffff 52%,
      #ffffff 60%, #d4e9a8 68%, var(--leaf-green) 76%, var(--leaf-green) 100%);
  }
  .sun-art {
    position: absolute;
    left: 40px; top: 36px;
    width: 180px; height: 170px;
    background: linear-gradient(135deg, var(--sun-yellow) 0%, var(--sun-orange) 50%, var(--sun-deep) 100%);
  }
  .front-name {
    position: absolute;
    left: 238px; top: 92px;
    font-size: 64px;
    line-height: 1;
    color: var(--brand-blue);
  }
  .service-divider {
    position: absolute;
    left: 336px; top: 150px;
    width: 2px; height: 62px;
    background: var(--brand-blue);
  }
  .service-list {
    position: absolute;
    left: 348px; top: 148px;
    list-style: none;
    color: var(--brand-blue);
    font-size: 17px;
    line-height: 21px;
  }
  .company-name {
    position: absolute;
    left: 0; right: 0; top: 232px;
    text-align: center;
    color: var(--brand-red);
    font-size: 21px;
  }
  .website {
    position: absolute;
    left: 0; right: 0; top: 278px;
    text-align: center;
    color: var(--brand-blue);
    font-size: 17px;
    letter-spacing: .5px;
  }

  /* Back side */
  .card--back {
    top: 520px;
    background: var(--leaf-green);
  }
  .contact {
    position: absolute;
    right: 34px; top: 26px;
    text-align: right;
    color: var(--brand-white);
    font-size: 14px;
    line-height: 18px;
  }
  .contact__name {
    font-family: var(--bold-font);
    font-weight: 700;
    color: var(--brand-blue);
    font-size: 17px;
    line-height: 20px;
  }
  .contact__title { margin-bottom: 12px; }
  .back-name {
    position: absolute;
    left: 34px; top: 186px;
    font-size: 72px;
    line-height: 1;
    color: var(--brand-white);
  }
  .back-company {
    position: absolute;
    left: 34px; top: 276px;
    color: var(--brand-blue);
    font-size: 18px;
  }
</style>
</head>
<body>
  <section class="card card--front" aria-label="Business card front">
    <div class="sun-art" role="img" aria-label="Illustration area: glowing orange sun over a green field"></div>
    <p class="front-name">7q</p>
    <div class="service-divider"></div>
    <ul class="service-list">
      <li>Home Inspections</li>
      <li>Environmental Testing</li>
      <li>Thermography Imaging</li>
    </ul>
    <p class="company-name">Seventh Quarry Solutions, LLC</p>
    <p class="website">www.7qSolutions.example</p>
  </section>

  <section class="card card--back" aria-label="Business card back">
    <div class="contact">
      <p class="contact__name">Gus Morrow</p>
      <p class="contact__title">President/CEO</p>
      <p>GusMorrow@7qSolutions.example</p>
      <p>555.014.7301</p>
      <p>Fax 555.014.7302</p>
    </div>
    <p class="back-name">7q</p>
    <p class="back-company">Seventh Quarry Solutions, LLC</p>
  </section>
</body>
</html>
```